Need web redesign for cybersecurity startup whose mission is to make robust cybersecurity protection

We need a web redesign for Velundra, a cyber security startup. We already have a logo and website but we’re looking for a redesign to reflect the new messaging and positioning of the company – and to update our look with a more polished feel. We’re looking for clean, powerful, confident designs that easily communicate the problems within the cybersecurity space and how Velundra is the answer to those problems.

We can have the long-scrolling stripe layout for the home page, but we don’t want a bunch of interior pages with the same long-scroll format. We’d like to do something a little different and easier to navigate.

Velundra’s products simplify and automate cybersecurity defense so non-experts can successfully protect their information and focus on their business. Velundra’s mission is to provide proactive cybersecurity protection that is easy to use, easy to implement and easy to afford. The designs should reflect this populist message as well as confidence and maybe a little irreverence. Additional key words to describe the company are: secure, protection, easy, everyone.

Velundra offers multiple security products which can both be purchased directly from their site. They provide the world’s most widely used WAF rule set for Wardplex as well as Velundra Guarded Linux (VGL) and Velundra Guarded Linux Kernels to protect Linux servers, IoT devices and Podlane containers.

Target Market(s)

IT leaders in small and mid-sized businesses, hosting providers, and enterprise dev ops, product and security groups

Industry/Entity Type

Security

Number of Pages Required

5+ page

Font styles to use
Serif
Sans Serif

Requirements
Must have
• - We can have the long-scrolling stripe layout for the home page, but we don’t want a bunch of interior pages with the same long-scroll format. We’d like to do something a little different and easier to navigate.
• - Clean, powerful, confident designs
• - Real imagery coupled with line designs
Nice to have
• Specific icons to be used for all marketing and web materials for each product:
• - Velund Guarded for Linux (VG/L)
• - WardPlex Rules
• - Velundra Guarded Linux Kernels
• - KRIVE - Commercial Support
• - Guarded OS for Podlane
• - Guarded Apps for Podlane
Should not have
• - No typical imagery for cybersecurity such as binary code, hooded figures, etc.

```html
<!DOCTYPE html>
<html lang="en">
<head>
<meta charset="utf-8">
<title>Velundra — Harden Your Shell Now</title>
<link href="https://fonts.googleapis.com/css2?family=Open+Sans:ital,wght@0,400;0,600;0,700;0,800;1,400&family=Lobster&display=swap" rel="stylesheet">
<style>
:root{
  --red:#e9574a;
  --red-deep:#e2453a;
  --ink:#2b2b2b;
  --ink-soft:#555;
  --muted:#8a8a8a;
  --paper:#ffffff;
  --mist:#ececec;
  --stone:#b6b6b6;
  --slate:#575757;
  --night:#1d1d1d;
  --tile:#777777;
}
*{margin:0;padding:0;box-sizing:border-box}
html,body{width:1200px;height:4215px;overflow:hidden}
body{position:relative;font-family:"Open Sans",Arial,sans-serif;color:var(--ink);background:var(--paper)}
.band{position:absolute;left:0;width:1200px;overflow:hidden}
.abs{position:absolute}
.center{left:0;width:1200px;text-align:center}
.fill{position:absolute}

/* hero */
.hero{top:0;height:655px}
.hero .photo{inset:0;background:radial-gradient(ellipse at 50% 40%,#6b6a3c 0%,#3f4a25 45%,#223016 100%)}
.brand{display:flex;align-items:center;gap:10px;font-weight:800;letter-spacing:2px}
.hero .brand{top:24px;left:520px;width:160px;justify-content:center;color:#fff;font-size:17px;flex-direction:column;gap:6px}
.brand .dot{width:34px;height:34px;border-radius:50%;background:var(--red)}
.nav-icons{top:40px;left:830px;display:flex;gap:34px;align-items:center}
.headline{top:500px;font-size:39px;font-weight:700;color:#fff;letter-spacing:-.3px}
.headline em{font-style:normal;color:var(--red)}

/* linux protection */
.linux{top:655px;height:399px;background:#ebebeb}
.linux .photo{left:155px;top:0;width:435px;height:399px;background:linear-gradient(135deg,#f4f4f4,#d8d8d8 60%,#cfcfcf)}
.linux .photo .brand{position:absolute;left:0;width:435px;top:180px;justify-content:center;color:var(--ink);font-size:18px}
.eyebrow{font-size:11px;font-weight:700;letter-spacing:1.5px;text-transform:uppercase;color:var(--red)}
.linux .eyebrow{left:655px;top:705px}
.linux h2{position:absolute;left:655px;top:724px;font-size:17px;font-weight:700;letter-spacing:.5px;text-transform:uppercase;color:var(--ink);white-space:nowrap}
.linux p{position:absolute;left:655px;top:758px;width:535px;font-size:10.5px;line-height:18px;color:var(--muted)}
.feature{display:flex;align-items:center;gap:10px}
.feature .ico{width:40px;height:40px;border-radius:50%;background:#3a3a3a;display:flex;align-items:center;justify-content:center}
.btn{display:inline-block;background:var(--red);color:#fff;font-size:10px;font-weight:700;letter-spacing:1px;text-transform:uppercase;text-align:center}
.feature .btn{width:116px;height:28px;line-height:28px}

/* trusted */
.trusted{top:1054px;height:303px;background:var(--red)}
.trusted .eyebrow{color:#fff;top:34px}
.trusted h2{top:56px;font-size:24px;font-weight:700;color:#2b2020;letter-spacing:.5px}
.rule{width:60px;height:1px;background:rgba(255,255,255,.6);left:570px}
.arrow-btn{width:30px;height:30px;border-radius:50%;border:1px solid rgba(255,255,255,.8);display:flex;align-items:center;justify-content:center}
.badge{width:74px;height:74px;border-radius:50%;background:#3a2c2a;top:114px}

/* video */
.video{top:1357px;height:393px;background:var(--slate)}
.video-card{left:310px;top:93px;width:540px;height:222px;background:#272727;text-align:center;color:#fff}
.video-card .kicker{font-size:13px;font-weight:600;margin-top:52px}
.video-card h2{font-size:26px;font-weight:800;letter-spacing:2px;margin-top:8px}
.play{width:50px;height:50px;border-radius:50%;background:var(--red);margin:20px auto 0;display:flex;align-items:center;justify-content:center}

/* quote */
.quote{top:1750px;height:447px}
.quote .photo{inset:0;background:linear-gradient(180deg,#6d7f95 0%,#b08a63 38%,#4a4640 55%,#1d1c1b 100%)}
.quote-badge{left:600px;top:78px;width:64px;height:64px;border-radius:50%;background:var(--red);display:flex;align-items:center;justify-content:center;color:#fff;font-size:42px;font-weight:800;font-family:Georgia,serif;line-height:1}
.quote-card{left:400px;top:138px;width:387px;height:205px;background:rgba(40,40,40,.82);text-align:center;color:#fff}
.quote-card h3{color:var(--red);font-size:30px;font-weight:800;letter-spacing:6px;margin-top:26px}
.quote-card p{font-size:10.5px;line-height:16px;font-style:italic;width:300px;margin:10px auto 0}
.quote-card .btn{margin-top:16px;padding:0 14px;height:26px;line-height:26px;text-transform:none;letter-spacing:.3px}

/* containers */
.containers{top:2197px;height:430px;background:var(--paper)}
.containers .photo{left:0;top:0;width:393px;height:430px;background:linear-gradient(160deg,#c9d4e2,#5d7596 45%,#2b3c58 80%)}
.script{left:400px;width:540px;top:96px;text-align:center;font-family:"Lobster",cursive;font-size:31px;color:var(--red)}
.containers p{position:absolute;left:430px;top:210px;width:440px;text-align:center;font-size:14px;line-height:24px;color:var(--ink);letter-spacing:.2px}

/* customers */
.customers{top:2627px;height:318px;background:var(--mist)}
.section-title{font-size:26px;font-weight:600;letter-spacing:1px;text-transform:uppercase}
.times{font-size:16px;color:var(--ink-soft)}
.segment{top:160px;width:180px;text-align:center;font-size:14px;font-weight:600;line-height:18px}
.segment svg{display:block;margin:0 auto 10px}

/* testimonials */
.voices{top:2945px;height:362px;background:var(--stone)}
.voices .kicker,.blog .kicker{font-size:10px;letter-spacing:1px;color:#555}
.voices h2{top:58px;font-size:22px;font-weight:800;letter-spacing:1px}
.avatar{left:568px;top:136px;width:64px;height:64px;border-radius:50%;background:#777}
.voices blockquote{top:220px;left:370px;width:460px;text-align:center;font-size:12px;line-height:20px;color:#333}
.cite{font-size:9px;letter-spacing:1px;font-weight:700;text-transform:uppercase}
.cite-co{font-size:9px;color:#444}

/* blog */
.blog{top:3307px;height:593px;background:var(--mist)}
.blog h2{top:48px;font-size:22px;font-weight:800;letter-spacing:1px}
.tile{width:240px;background:var(--tile)}
.tile.feature-post{background:#242424;color:#fff;text-align:center}
.tile.feature-post .eyebrow{margin-top:70px}
.tile.feature-post h4{font-size:16px;font-weight:600;letter-spacing:1px;margin-top:6px}
.tile .go{width:30px;height:30px;border-radius:50%;background:#fff;margin:18px auto 0;display:flex;align-items:center;justify-content:center}

/* subscribe */
.subscribe{left:323px;top:3887px;width:534px;height:33px;display:flex;z-index:3}
.subscribe .field{flex:1;background:#fff;font-size:10px;color:#999;padding:0 16px;line-height:33px}
.subscribe .btn{width:104px;line-height:33px}

/* footer */
.footer{top:3900px;height:273px;background:var(--night);color:#aaa}
.footer .brand{top:52px;left:500px;width:200px;justify-content:center;color:#fff;font-size:16px}
.footer p{top:118px;left:330px;width:540px;text-align:center;font-size:10px;line-height:18px;color:#999}
.socials{top:192px;left:0;width:1200px;display:flex;justify-content:center;gap:10px}
.socials span{width:20px;height:20px;background:#3a3a3a}
.contact{top:238px;left:0;width:1200px;display:flex;justify-content:center;gap:56px;font-size:10px;color:#bbb}
.contact span{display:flex;align-items:center;gap:8px}
.legal{top:4173px;height:42px;background:#121212;color:#888;font-size:10px}
.legal .copy{left:230px;top:14px}
.cards{right:230px;top:12px;display:flex;gap:5px}
.cards span{width:26px;height:17px;background:#d8d8d8;border-radius:2px}
</style>
</head>
<body>

<header class="band hero">
  <div class="fill photo" role="img" aria-label="Aerial photo of a road cutting through a dense autumn forest with a glowing line-drawn globe above it"></div>
  <div class="abs brand"><span class="dot"></span>VELUNDRA</div>
  <nav class="abs nav-icons" aria-label="Site tools">
    <svg width="20" height="20" viewBox="0 0 20 20" fill="none" stroke="#fff" stroke-width="1.6"><path d="M2 3h3l2 10h9l2-7H6"/><circle cx="8" cy="17" r="1.2"/><circle cx="15" cy="17" r="1.2"/><circle cx="17" cy="3" r="3" fill="#e9574a" stroke="none"/></svg>
    <svg width="18" height="18" viewBox="0 0 18 18" fill="none" stroke="#fff" stroke-width="2"><circle cx="7.5" cy="7.5" r="5"/><path d="M11.5 11.5l5 5"/></svg>
    <svg width="22" height="18" viewBox="0 0 22 18" stroke="#fff" stroke-width="2"><path d="M1 3h20M1 9h20M1 15h20"/></svg>
  </nav>
  <h1 class="abs center headline">Don’t Be the Next Cyber Victim. <em>Harden Your Shell Now.</em></h1>
</header>

<section class="band linux">
  <div class="fill photo" role="img" aria-label="Faded photo of a man in a suit holding the company name card"><div class="brand"><span class="dot"></span>VELUNDRA</div></div>
</section>
<div class="abs eyebrow" style="left:655px;top:705px">Linux Protection</div>
<h2 class="abs" style="left:655px;top:724px;font-size:17px;font-weight:700;letter-spacing:.5px;white-space:nowrap">LINUX SERVER PROTECTION FOR EVERYONE AND EVERYTHING</h2>
<p class="abs" style="left:655px;top:758px;width:535px;font-size:10.5px;line-height:18px;color:var(--muted)">Cyber attacks happen. The question is, are you ready? Far too many small and mid-sized teams believe they are safe because they don't think cyber protection is accessible or made for their needs. Every business needs it. Velundra protects Linux servers, web apps, IoT devices and Podlane containers. It only takes a couple of clicks to get complete protection.</p>
<div class="abs feature" style="left:655px;top:857px"><span class="ico"><svg width="16" height="16" viewBox="0 0 16 16" fill="none" stroke="#fff" stroke-width="1.5"><path d="M8 1l6 3v4c0 4-3 6-6 7-3-1-6-3-6-7V4z"/></svg></span><span class="btn">Why Velundra</span></div>
<div class="abs feature" style="left:843px;top:857px"><span class="ico"><svg width="16" height="16" viewBox="0 0 16 16" fill="none" stroke="#fff" stroke-width="1.5"><rect x="2" y="2" width="12" height="5"/><rect x="2" y="9" width="12" height="5"/></svg></span><span class="btn">Linux Servers</span></div>
<div class="abs feature" style="left:655px;top:913px"><span class="ico"><svg width="16" height="16" viewBox="0 0 16 16" fill="none" stroke="#fff" stroke-width="1.5"><rect x="4" y="1" width="8" height="14" rx="1.5"/><path d="M7 12h2"/></svg></span><span class="btn">IoT Devices</span></div>
<div class="abs feature" style="left:843px;top:913px"><span class="ico"><svg width="16" height="16" viewBox="0 0 16 16" fill="none" stroke="#fff" stroke-width="1.5"><rect x="1" y="5" width="14" height="8"/><path d="M5 5v8M10 5v8"/></svg></span><span class="btn">Podlane Containers</span></div>

<section class="band trusted">
  <div class="abs center eyebrow" style="color:#fff;top:36px;font-size:10px">Trusted by Thousands</div>
  <h2 class="abs center" style="top:56px;font-size:24px;font-weight:700;color:#2b2020;letter-spacing:.5px">MORE THAN 20,000 SERVERS PROTECTED</h2>
  <div class="abs rule" style="top:98px"></div>
  <div class="abs arrow-btn" style="left:275px;top:139px"><svg width="10" height="10" viewBox="0 0 10 10" stroke="#fff" stroke-width="1.5" fill="none"><path d="M7 1L3 5l4 4"/></svg></div>
  <div class="abs arrow-btn" style="left:895px;top:139px"><svg width="10" height="10" viewBox="0 0 10 10" stroke="#fff" stroke-width="1.5" fill="none"><path d="M3 1l4 4-4 4"/></svg></div>
  <div class="abs badge" style="left:333px"></div>
  <div class="abs badge" style="left:433px;border-radius:8px"></div>
  <div class="abs badge" style="left:533px"></div>
  <div class="abs badge" style="left:633px;border-radius:8px"></div>
  <div class="abs badge" style="left:733px"></div>
  <div class="abs badge" style="left:833px;border-radius:8px"></div>
</section>

<section class="band video">
  <div class="abs video-card">
    <div class="kicker">Harden Your Shell Now</div>
    <h2>WATCH OUR VIDEO EXPLAINER</h2>
    <div class="play"><svg width="14" height="16" viewBox="0 0 14 16"><path d="M2 1l11 7-11 7z" fill="#fff"/></svg></div>
  </div>
</section>

<section class="band quote">
  <div class="fill photo" role="img" aria-label="Photo of a rocky shoreline at sunset over calm water"></div>
  <div class="abs quote-badge">“</div>
  <div class="abs quote-card">
    <h3>QUOTE:”</h3>
    <p>“We found our server security in Velundra Guarded Linux because it works. We've used it for years and it has been essential in keeping web hosts at bay.”</p>
    <span class="btn">Julian Mercer, Hostvale</span>
  </div>
</section>

<section class="band containers">
  <div class="fill photo" role="img" aria-label="Cut-out silhouette of a businessman filled with a blue city photo"></div>
  <h2 class="abs script">Yes. You Can Secure Podlane Containers</h2>
  <p>Podlane is the fastest growing application developer software in the world. But, people don't realize that their containers are wide open to cyber attacks. Velundra provides a secure OS kernel that is inherited by all containers on a single server. It's easy to install, doesn't impact performance and protects your containers against malicious attacks immediately.</p>
</section>

<section class="band customers">
  <h2 class="abs center section-title" style="top:62px">Customers</h2>
  <div class="abs center times" style="top:102px">×</div>
  <div class="abs segment" style="left:219px"><svg width="26" height="26" viewBox="0 0 26 26" fill="none" stroke="#333" stroke-width="1.4"><path d="M13 2l10 5v12l-10 5-10-5V7z M3 7l10 5 10-5 M13 12v12"/></svg>Hosting Providers</div>
  <div class="abs segment" style="left:405px"><svg width="26" height="26" viewBox="0 0 26 26" fill="none" stroke="#333" stroke-width="1.4"><circle cx="13" cy="9" r="5"/><path d="M3 24c1-6 5-9 10-9s9 3 10 9"/></svg>Mid-sized &amp;<br>Small Business</div>
  <div class="abs segment" style="left:596px"><svg width="26" height="26" viewBox="0 0 26 26" fill="none" stroke="#333" stroke-width="1.4"><path d="M13 2l10 5v12l-10 5-10-5V7z M3 7l10 5 10-5 M13 12v12"/></svg>Enterprises</div>
  <div class="abs segment" style="left:790px"><svg width="26" height="26" viewBox="0 0 26 26" fill="none" stroke="#333" stroke-width="1.4"><circle cx="13" cy="13" r="11"/><ellipse cx="13" cy="13" rx="5" ry="11"/><path d="M2 13h22"/></svg>IoT OEMs</div>
</section>

<section class="band voices">
  <div class="abs center kicker" style="top:40px">Recognition wherever matters</div>
  <h2 class="abs center" style="top:56px;font-size:22px;font-weight:800;letter-spacing:1px">THEY SAY ABOUT US</h2>
  <div class="abs center times" style="top:90px">×</div>
  <div class="abs avatar" role="img" aria-label="Reviewer portrait placeholder"></div>
  <blockquote class="abs">“Velundra eliminated 90% of our shared server issues overnight. And, it saves us about four hours of staff time every day because it protects servers automatically.”
    <div class="cite" style="margin-top:14px">Stellan Kirby</div>
    <div class="cite-co">Brightcrate</div>
  </blockquote>
  <div class="abs arrow-btn" style="left:255px;top:235px;border-color:#777"><svg width="10" height="10" viewBox="0 0 10 10" stroke="#555" stroke-width="1.5" fill="none"><path d="M7 1L3 5l4 4"/></svg></div>
  <div class="abs arrow-btn" style="left:873px;top:235px;border-color:#777"><svg width="10" height="10" viewBox="0 0 10 10" stroke="#555" stroke-width="1.5" fill="none"><path d="M3 1l4 4-4 4"/></svg></div>
</section>

<section class="band blog">
  <div class="abs center kicker" style="top:28px">Keep Updated</div>
  <h2 class="abs center" style="top:44px;font-size:22px;font-weight:800;letter-spacing:1px">LASTEST ON OUR BLOG</h2>
  <div class="abs center times" style="top:78px">×</div>
  <article class="abs tile feature-post" style="left:242px;top:113px;height:218px">
    <div class="eyebrow">Security</div>
    <h4>UPGRADE YOUR SECURITY</h4>
    <div class="go"><svg width="12" height="12" viewBox="0 0 12 12" stroke="#222" stroke-width="1.6" fill="none"><path d="M2 10L10 2M4 2h6v6"/></svg></div>
  </article>
  <div class="abs tile" style="left:487px;top:113px;height:218px"></div>
  <div class="abs tile" style="left:732px;top:113px;height:218px"></div>
  <div class="abs tile" style="left:242px;top:336px;height:216px"></div>
  <div class="abs tile" style="left:487px;top:336px;height:216px"></div>
  <div class="abs tile" style="left:732px;top:336px;height:216px"></div>
</section>

<form class="abs subscribe"><span class="field">Enter your email</span><span class="btn">Subscribe</span></form>

<footer class="band footer">
  <div class="abs brand"><span class="dot" style="width:26px;height:26px"></span>VELUNDRA</div>
  <p class="abs">Simple, proactive server protection for everyone. Guard your Linux servers, web apps and containers in minutes, with expert rules kept current around the clock.</p>
  <div class="abs socials"><span></span><span></span><span></span><span></span><span></span><span></span></div>
  <div class="abs contact">
    <span><svg width="10" height="12" viewBox="0 0 10 12" fill="#e9574a"><path d="M5 0a4 4 0 014 4c0 3-4 8-4 8S1 7 1 4a4 4 0 014-4z"/></svg>Harrow Lane, Pell City, USA</span>
    <span><svg width="12" height="9" viewBox="0 0 12 9" fill="none" stroke="#e9574a" stroke-width="1.3"><rect x=".5" y=".5" width="11" height="8"/><path d="M.5.5L6 5l5.5-4.5"/></svg>hello@velundra-mail.com</span>
    <span><svg width="11" height="11" viewBox="0 0 11 11" fill="#e9574a"><path d="M2 0l2 2.5-1 1.5c1 1.5 2 2.5 3.5 3.5l1.5-1L11 8.5 9 11C4 10 1 7 0 2z"/></svg>+000 55120 - +000 55198</span>
  </div>
</footer>
<div class="band legal">
  <div class="abs copy">© Copyright VELUNDRA 2017. All Rights Reserved</div>
  <div class="abs cards"><span></span><span></span><span></span><span></span><span></span></div>
</div>

</body>
</html>
```